WebDesign | Financial Services Firm - Risk Mitigation

We are a professional services consulting firm that specializes in high net worth individuals over $25,000,000, executives C-suite and above, closely held businesses owners, family offices and highly compensated employees.

Our focus is on risk mitigation and tax efficient strategies. Our clients take their risk on themselves and have a proven track record generating wealth. Our directive is to preserve and protect the wealth they’ve already created.

Our company Harbor Crest Advisory is geared around five directives of asset protection:
1) Legal Structuring
2) Leverage & Financing
3) Risk Management - Asset Protection & Insurance, Trustee Work
4) Asset Management & Investing - Under www.tqlvalemark.com
5) Tax Efficient Strategies

Our Company Mark is a Pentagon with a key in the middle. A pentagon is the most efficient defensive structure. Each point of a pentagon is equal distance front every point . Each side provides support to another and works together, which is the key to our clients success.

Our key colors are blue, black and silver.

We ‘re located in the Pacific Northwest with bi coastal and international clients. We have fewer, higher net worth clients and provide exceptional customer service. We do not do social media.

We'll need the following pages:
-Front Landing Page.
Front page has to have link to hbportal.docuvaultix.com for logging into secure site.
- Contact & About Us Page
- Our Team Page
- Five Sides of Wealth Management
> Legal & Business Structuring
> Leverage & Financing
> Risk Management & Asset Protection.
> Asset Management and Investing - Will link to TQL (won't be turned on for a few months)
> Tax Efficient Strategies.

Industry/Entity Type

Financial Service

Coding

Coded - Design and coding required

Number of Pages Required

5+ page

Font styles to use
Sans Serif

Colors
0555a3

Requirements
Must have
• Our key colors are blue, black and silver.

-Front Landing Page.
- Contact & About Us Page
- Our Team Page
> Leverage & Financing
Nice to have
• I have attached images that have been purchased for use on the webpage. Us or not.

location page: 847 W Alder Ln, Suite 412, Lake Oswego, OR 97035
Should not have
• lots of color.

```html
<!DOCTYPE html>
<html lang="en">
<head>
<meta charset="utf-8">
<title>Harbor Crest Advisory — Financial Services Firm</title>
<link href="https://fonts.googleapis.com/css2?family=Fira+Sans:wght@500;600;700&family=Lato:wght@400;700&display=swap" rel="stylesheet">
<style>
:root{
  --blue:#0b3d91;
  --blue-bright:#0555a3;
  --ink:#222222;
  --text:#3a3a3a;
  --muted:#555;
  --silver:#efefef;
  --line:#d8d8d8;
  --footer:#1f1f1f;
  --footer-text:#cfcfcf;
  --white:#ffffff;
}
*{box-sizing:border-box;margin:0;padding:0}
html,body{width:1200px;height:3431px;overflow:hidden;background:var(--white)}
body{position:relative;font-family:"Lato",sans-serif;color:var(--text)}
.abs{position:absolute}
h1,h2,h3,.display{font-family:"Fira Sans",sans-serif}

/* header */
.site-header{left:0;top:0;width:1200px;height:114px;background:var(--white)}
.brand{left:76px;top:34px;display:flex;align-items:center;gap:12px}
.brand-mark{width:40px;height:40px;border-radius:50%;background:var(--blue)}
.brand-name{font-family:"Lato",sans-serif;font-weight:700;font-size:22px;color:var(--blue);letter-spacing:1px}
.nav a{position:absolute;top:69px;font-size:12.5px;font-weight:700;color:#333;text-decoration:none;letter-spacing:.2px}
.nav .active{color:var(--blue)}
.nav-dot{left:452px;top:42px;width:18px;height:18px;border-radius:50%;background:var(--blue)}

/* hero */
.hero{left:0;top:114px;width:1200px;height:660px;
  background:linear-gradient(180deg,#2b3a6b 0%,#4b4f7d 25%,#3a3240 55%,#5a4436 80%,#6e5a4a 100%)}
.hero-title{left:0;top:200px;width:1200px;text-align:center;color:var(--white);font-weight:700;font-size:88px;line-height:110px;letter-spacing:1px}
.hero-sub{left:0;top:314px;width:1200px;text-align:center;color:var(--white);font-weight:600;font-size:30px;line-height:40px}
.btn{display:flex;align-items:center;justify-content:center;background:var(--blue);color:var(--white);font-weight:700;font-size:16px;text-decoration:none}
.hero-btn{left:516px;top:394px;width:170px;height:42px}

/* section heads */
.section-title{left:0;width:1200px;text-align:center;color:var(--ink);font-weight:600;font-size:36px}

/* services */
.arrow{width:30px;height:44px}
.service{width:238px;height:266px;border:1px solid var(--line);border-bottom:4px solid var(--blue);background:var(--white);text-align:center;padding-top:26px}
.service svg{width:56px;height:60px}
.service h3{margin-top:14px;font-weight:500;font-size:22px;line-height:27px;color:var(--blue)}
.service p{margin:8px auto 0;width:180px;font-size:14px;line-height:23px;color:var(--muted)}

/* welcome */
.welcome{left:0;top:1250px;width:1200px;height:470px;background:var(--silver)}
.welcome h2{left:76px;top:104px;font-weight:600;font-size:38px;color:var(--ink)}
.welcome p{left:76px;top:166px;width:500px;font-size:17px;line-height:31px;color:var(--text)}
.welcome .btn{left:76px;top:318px;width:168px;height:41px}
.welcome-photo{left:613px;top:0;width:587px;height:470px}

/* team */
.member-band{background:var(--blue);color:var(--white)}
.member-band h3{font-weight:600;font-size:25px}
.member-band p{margin-top:12px;font-size:14px;line-height:27px}
.member-band a{display:inline-block;margin-top:10px;font-size:14px;font-weight:700;color:var(--white)}

/* news */
.news{left:0;top:2462px;width:1200px;height:611px;background:var(--silver)}
.news-img{top:130px;height:221px}
.news h3{top:378px;font-weight:600;font-size:21px;color:var(--ink);white-space:nowrap}
.news p{top:410px;font-size:14px;line-height:25px;color:var(--muted)}
.news .btn{top:503px;width:168px;height:41px}

/* footer */
.site-footer{left:0;top:3073px;width:1200px;height:358px;background:var(--footer);color:var(--footer-text)}
.foot-brand{left:76px;top:90px;width:215px;text-align:center}
.foot-brand .brand-mark{margin:0 auto 18px;width:62px;height:62px;background:var(--blue-bright)}
.foot-brand span{font-weight:700;font-size:19px;color:var(--white);letter-spacing:.5px;white-space:nowrap}
.foot-head{font-size:15px;font-weight:700;color:var(--white);letter-spacing:.3px}
.foot-list a,.foot-list div{display:block;font-size:13px;color:var(--footer-text);text-decoration:none;line-height:29px}
.foot-list .contact-row{display:flex;align-items:center;gap:20px}
.contact-row svg{width:12px;height:12px;fill:var(--footer-text);flex:none}
.signup{left:885px;top:95px;width:242px;height:44px;display:flex}
.signup input{flex:1;min-width:0;border:0;padding:0 15px;font-family:"Lato",sans-serif;font-size:13px;color:#555}
.signup button{width:46px;border:0;background:var(--blue-bright);display:flex;align-items:center;justify-content:center}
.foot-rule{left:0;top:297px;width:1200px;height:1px;background:#333}
.copyright{left:76px;top:319px;font-size:12px;color:var(--footer-text)}
.social{top:319px;width:18px;height:18px;border-radius:3px;background:var(--footer-text)}
</style>
</head>
<body>

<header class="site-header abs">
  <div class="brand abs"><span class="brand-mark"></span><span class="brand-name">Harbor Crest Advisory</span></div>
  <nav class="nav">
    <span class="nav-dot abs"></span>
    <a class="active" href="#" style="left:442px">HOME</a>
    <a href="#" style="left:519px">ABOUT US</a>
    <a href="#" style="left:620px">WEALTH MANAGEMENT</a>
    <a href="#" style="left:808px">OUR TEAM</a>
    <a href="#" style="left:911px">NEWS &amp; MEDIA</a>
    <a href="#" style="left:1043px">CONTACT US</a>
  </nav>
</header>

<section class="hero abs" role="img" aria-label="Evening street scene with a lit building and light trails from traffic">
  <h1 class="hero-title abs">Harbor Crest Advisory</h1>
  <div class="hero-sub abs display">We are a Financial Services Firm - Risk Mitigation</div>
  <a class="btn abs hero-btn" href="#">Read More</a>
</section>

<h2 class="section-title abs" style="top:828px">Wealth Management</h2>

<svg class="arrow abs" style="left:34px;top:1018px" viewBox="0 0 30 44"><path d="M24 4 6 22l18 18" fill="none" stroke="#222" stroke-width="3"/></svg>
<svg class="arrow abs" style="left:1138px;top:1018px" viewBox="0 0 30 44"><path d="M6 4l18 18L6 40" fill="none" stroke="#222" stroke-width="3"/></svg>

<article class="service abs" style="left:75px;top:910px">
  <svg viewBox="0 0 56 60"><path d="M10 3h26l12 12v42H10z" fill="none" stroke="#0b3d91" stroke-width="5" stroke-linejoin="round"/><path d="M19 28h20M19 37h20M19 46h20" stroke="#0b3d91" stroke-width="4"/></svg>
  <h3>Legal &amp; Business<br>Structuring</h3>
  <p>Sunt in culpa qui officia deserunt mollit anim id est laborum perspiciatis</p>
</article>
<article class="service abs" style="left:345px;top:910px">
  <svg viewBox="0 0 76 60"><rect x="3" y="10" width="70" height="40" fill="#0b3d91"/><rect x="12" y="17" width="52" height="26" rx="4" fill="#fff"/><circle cx="38" cy="30" r="10" fill="#0b3d91"/><text x="38" y="35" font-size="14" font-weight="700" fill="#fff" text-anchor="middle" font-family="Lato,sans-serif">1</text></svg>
  <h3>Leverage<br>&amp; Financing</h3>
  <p>Sunt in culpa qui officia deserunt mollit anim id est laborum perspiciatis</p>
</article>
<article class="service abs" style="left:616px;top:910px">
  <svg viewBox="0 0 60 60"><path d="M10 26A20 20 0 0 1 46 16" fill="none" stroke="#0b3d91" stroke-width="7"/><path d="M40 6l14 2-4 14z" fill="#0b3d91"/><path d="M50 34A20 20 0 0 1 14 44" fill="none" stroke="#0b3d91" stroke-width="7"/><path d="M20 54L6 52l4-14z" fill="#0b3d91"/></svg>
  <h3>Risk<br>Management</h3>
  <p>Sunt in culpa qui officia deserunt mollit anim id est laborum perspiciatis</p>
</article>
<article class="service abs" style="left:887px;top:910px">
  <svg viewBox="0 0 56 60"><rect x="4" y="2" width="48" height="56" rx="4" fill="#0b3d91"/><rect x="11" y="9" width="34" height="12" fill="#fff"/><g fill="#fff"><rect x="11" y="27" width="8" height="8"/><rect x="24" y="27" width="8" height="8"/><rect x="37" y="27" width="8" height="22"/><rect x="11" y="41" width="8" height="8"/><rect x="24" y="41" width="8" height="8"/></g></svg>
  <h3>Tax Efficient<br>Strategies</h3>
  <p>Sunt in culpa qui officia deserunt mollit anim id est laborum perspiciatis</p>
</article>

<section class="welcome abs">
  <h2 class="abs">Welcome to Our Website</h2>
  <p class="abs">We are a professional services consulting firm that specializes in high net worth individuals over $25,000,000, executives C-suite and above, closely held &nbsp;businesses owners, family offices and highly compensated employees.</p>
  <a class="btn abs" href="#">Read More</a>
  <svg class="welcome-photo abs" viewBox="0 0 587 470" role="img" aria-label="Stacks of coins resting on euro banknotes">
    <defs><linearGradient id="coinTone" x1="0" y1="0" x2="1" y2="1"><stop offset="0" stop-color="#8a7fb0"/><stop offset=".45" stop-color="#b88a5e"/><stop offset="1" stop-color="#c45a6a"/></linearGradient></defs>
    <polygon points="240,0 587,0 587,470 100,470 0,170" fill="url(#coinTone)"/>
  </svg>
</section>

<h2 class="section-title abs" style="top:1773px">Our Team</h2>

<div class="member-band abs" style="left:345px;top:1886px;width:691px;height:203px;padding:26px 40px 0 138px">
  <h3>Marcus Ellery</h3>
  <p>Marcus Ellery is the Financial Strategist and Founder who partners with C-Suite Executives, Family Offices, Real Estate Investors and Closely Held Business Owners to protect and maximize their wealth.</p>
  <a href="#">Read More &nbsp;&gt;&gt;</a>
</div>
<svg class="abs" style="left:163px;top:1860px" width="276" height="255" viewBox="0 0 276 255" role="img" aria-label="Portrait of the founder">
  <polygon points="134,2 274,98 220,252 46,252 2,100" fill="#fff"/>
  <polygon points="134,10 264,100 214,245 52,245 10,102" fill="#7a8a6a"/>
</svg>

<div class="member-band abs" style="left:164px;top:2151px;width:690px;height:203px;padding:26px 140px 0 34px">
  <h3>Owen Hartwell</h3>
  <p>Owen Hartwell is the CFO and Strategist for our closely held businesses. As a former CPA, he takes in-depth roles in closely held companies as a financial consultant during times of exit or transition.</p>
  <a href="#">Read More &nbsp;&gt;&gt;</a>
</div>
<svg class="abs" style="left:762px;top:2125px" width="276" height="255" viewBox="0 0 276 255" role="img" aria-label="Portrait of the chief financial officer">
  <polygon points="140,2 274,100 232,252 56,252 2,100" fill="#fff"/>
  <polygon points="140,10 266,102 226,245 62,245 10,102" fill="#6a5a52"/>
</svg>

<section class="news abs">
  <h2 class="section-title abs" style="top:52px">Latest News</h2>
  <div class="news-img abs" style="left:75px;width:512px;background:linear-gradient(180deg,#4a5a7a,#6a4a3a 70%,#3a2e2a)" role="img" aria-label="Brick office building at dusk"></div>
  <div class="news-img abs" style="left:615px;width:241px;background:linear-gradient(135deg,#8a7fb0,#b88a5e 55%,#c45a6a)" role="img" aria-label="Coins stacked on banknotes"></div>
  <div class="news-img abs" style="left:884px;width:242px;background:linear-gradient(135deg,#2e3a3a,#6a6a4a 55%,#3a3228)" role="img" aria-label="Old vault door with locking mechanism"></div>

  <h3 class="abs" style="left:76px">Excepteur sint occaecat cupidatat non proident..</h3>
  <h3 class="abs" style="left:616px">Excepteur sint occaecat..</h3>
  <h3 class="abs" style="left:885px">Excepteur sint occaecat..</h3>

  <p class="abs" style="left:76px;width:510px">Sunt in culpa qui officia deserunt mollit anim id est laborum perspiciatis unde omnis iste natus error sit voluptatem accusantium laudantium, totam rem aperiam, eaque ipsa quae ab illo inventore veritatis et quaa.. .</p>
  <p class="abs" style="left:616px;width:240px">Sunt in culpa qui officia deserunt mollit anim id est laborum unde omnis iste natus error...</p>
  <p class="abs" style="left:885px;width:240px">Sunt in culpa qui officia deserunt mollit anim id est laborum unde omnis iste natus error...</p>

  <a class="btn abs" href="#" style="left:76px">Read More</a>
  <a class="btn abs" href="#" style="left:615px">Read More</a>
  <a class="btn abs" href="#" style="left:884px">Read More</a>
</section>

<footer class="site-footer abs">
  <div class="foot-brand abs"><div class="brand-mark"></div><span>Harbor Crest Advisory</span></div>

  <div class="foot-head abs" style="left:349px;top:60px">SITE MAP</div>
  <div class="foot-list abs" style="left:349px;top:92px"><a href="#">Home</a><a href="#">About Us</a><a href="#">Who We Serve</a><a href="#">Capabilities</a></div>
  <div class="foot-list abs" style="left:482px;top:92px"><a href="#">Brands</a><a href="#">News &amp; Media</a><a href="#">Contact Us</a></div>

  <div class="foot-head abs" style="left:635px;top:60px">CONTACT INFO</div>
  <div class="foot-list abs" style="left:635px;top:94px">
    <div style="line-height:22px">52 Linden Court, Suite 3<br>Portland, OR, USA</div>
    <div class="contact-row"><svg viewBox="0 0 12 12"><path d="M2 1l3 0 1 3-2 1a7 7 0 0 0 3 3l1-2 3 1v3c-6 0-10-4-9-9z"/></svg>1-800-555-0142</div>
    <div class="contact-row"><svg viewBox="0 0 12 12"><path d="M0 2h12v1L6 7 0 3zM0 4l6 4 6-4v6H0z"/></svg>info@companyname.com</div>
    <div class="contact-row"><svg viewBox="0 0 12 12"><path d="M6 0a4 4 0 0 1 4 4c0 3-4 8-4 8S2 7 2 4a4 4 0 0 1 4-4zm0 2.5a1.5 1.5 0 1 0 0 3 1.5 1.5 0 0 0 0-3z"/></svg>Map Direction</div>
  </div>

  <div class="foot-head abs" style="left:885px;top:60px">EMAIL SIGN UP</div>
  <form class="signup abs"><input type="email" placeholder="Enter Email Address"><button type="button" aria-label="Subscribe"><svg width="12" height="16" viewBox="0 0 12 16"><path d="M2 2l7 6-7 6" fill="none" stroke="#fff" stroke-width="2.5"/></svg></button></form>

  <div class="foot-rule abs"></div>
  <div class="copyright abs">Copyright © 2021, Company Name All Right reserved</div>
  <span class="social abs" style="left:952px"></span>
  <span class="social abs" style="left:988px"></span>
  <span class="social abs" style="left:1028px"></span>
  <span class="social abs" style="left:1068px"></span>
  <span class="social abs" style="left:1108px"></span>
</footer>

</body>
</html>
```